BRISKA sparkling water needs new artwork! Based in Southern California

"Briska" is a new sparkling water company based in Southern California that offers refreshing flavors (lime, cherry, & mango) with B vitamins and antioxidants.

We would like to see packaging designs for standard 12oz cans for each of the three flavors.
Our initial preference is to have individual artwork for each flavor.

Attached are examples of competitors' designs.
Updates

We are extending the deadline for the Thanksgiving Holiday. Thank you all for your contributions.

```html
<!DOCTYPE html>
<html lang="en">
<head>
<meta charset="utf-8">
<title>Briska Sparkling Water – Cherry can label</title>
<link rel="stylesheet" href="https://fonts.googleapis.com/css2?family=Oswald:wght@500;700&family=Montserrat:wght@400;500&family=Kaushan+Script&family=Righteous&display=swap">
<style>
  :root {
    --backdrop: #a01418;
    --brand-red: #c8141b;
    --deep-red: #9c0a0e;
    --label-white: #f2f2f2;
    --ink: #141414;
    --art-light: #f4dcdc;
    --art-mid: #b8312c;
  }
  * { margin: 0; padding: 0; box-sizing: border-box; }
  html, body { width: 1200px; height: 1133px; overflow: hidden; }
  body {
    background: var(--backdrop);
    position: relative;
    font-family: "Montserrat", sans-serif;
  }
  .can-label {
    position: absolute;
    left: 320px;
    top: 100px;
    width: 560px;
    height: 930px;
    border-radius: 18px;
    overflow: hidden;
    background: var(--label-white);
    box-shadow: 0 24px 50px rgba(0,0,0,0.35);
  }
  .label-bands { position: absolute; inset: 0; }
  .brand-name {
    position: absolute;
    top: 40px;
    width: 100%;
    text-align: center;
    font-family: "Oswald", sans-serif;
    font-weight: 700;
    font-size: 140px;
    line-height: 1;
    letter-spacing: 2px;
    color: var(--brand-red);
  }
  .product-type {
    position: absolute;
    top: 196px;
    width: 100%;
    text-align: center;
    font-family: "Kaushan Script", cursive;
    font-size: 58px;
    line-height: 1.2;
    color: var(--ink);
  }
  .tagline-rule {
    position: absolute;
    top: 290px;
    left: 30px;
    right: 30px;
    display: flex;
    align-items: center;
    gap: 14px;
    font-size: 15px;
    font-weight: 500;
    letter-spacing: 1.5px;
    color: var(--ink);
  }
  .tagline-rule::before, .tagline-rule::after {
    content: "";
    flex: 1;
    height: 1.5px;
    background: var(--ink);
  }
  .fruit-art {
    position: absolute;
    left: 140px;
    top: 340px;
    width: 290px;
    height: 300px;
    border-radius: 50%;
    background: radial-gradient(circle at 50% 55%, var(--art-mid) 0%, #d98a86 45%, var(--art-light) 75%, var(--label-white) 100%);
  }
  .flavor-name {
    position: absolute;
    top: 680px;
    width: 100%;
    text-align: center;
    font-family: "Righteous", sans-serif;
    font-size: 76px;
    line-height: 1.1;
    letter-spacing: 2px;
    color: transparent;
    -webkit-text-stroke: 2.5px #ffffff;
  }
  .label-details {
    position: absolute;
    top: 775px;
    width: 100%;
    text-align: center;
    color: #ffffff;
  }
  .benefits { font-size: 19px; font-weight: 500; letter-spacing: 1px; }
  .maker {
    margin-top: 8px;
    font-family: "Oswald", sans-serif;
    font-weight: 500;
    font-size: 17px;
    letter-spacing: 0.5px;
  }
  .origin { margin-top: 4px; font-size: 13px; letter-spacing: 0.8px; }
  .volume {
    margin-top: 10px;
    font-family: "Oswald", sans-serif;
    font-weight: 500;
    font-size: 34px;
  }
</style>
</head>
<body>
  <main class="can-label">
    <svg class="label-bands" width="560" height="930" viewBox="0 0 560 930" aria-hidden="true">
      <defs>
        <linearGradient id="red-band" x1="0" y1="0" x2="1" y2="1">
          <stop offset="0" stop-color="#c8141b"/>
          <stop offset="1" stop-color="#9c0a0e"/>
        </linearGradient>
      </defs>
      <path d="M0,470 C170,420 380,395 560,360 L560,930 L0,930 Z" fill="url(#red-band)"/>
      <path d="M0,505 C170,452 380,425 560,392" fill="none" stroke="#f2f2f2" stroke-width="16"/>
      <path d="M0,548 C170,490 380,462 560,430" fill="none" stroke="#f2f2f2" stroke-width="10"/>
      <path d="M0,600 C170,545 360,515 560,490 L560,930 L0,930 Z" fill="url(#red-band)"/>
    </svg>

    <h1 class="brand-name">BRISKA</h1>
    <p class="product-type">Sparkling Water</p>
    <p class="tagline-rule">REFRESHING FLAVORS</p>

    <div class="fruit-art" role="img" aria-label="Illustration of a bunch of glossy red cherries with a green leaf inside a sunburst frame"></div>

    <p class="flavor-name">CHERRY</p>
    <div class="label-details">
      <p class="benefits">B VITAMINS AND ANTIOXIDANTS</p>
      <p class="maker">CREATED BY BRISKA</p>
      <p class="origin">Based in Southern California</p>
      <p class="volume">12oz</p>
    </div>
  </main>
</body>
</html>
```